Luxury Eco accommodation needs new website

Luxury lodge accommodation on exclusive private property in Flinders Ranges South Australia.
Brand new venture needs new site.
Focus on small group accommodation on exclusive property with outdoor experiences. Mountain biking , bush walking, outdoor dining.
We currently have a website but are having trouble making it our own. Needs to be "polished" by a professional.
Can you help?

www.larkhollowretreat.com.au

Target Market(s)

High income travellers, luxury accommodation

Industry/Entity Type

Accommodation

```html
<!DOCTYPE html>
<html lang="en">
<head>
<meta charset="utf-8">
<title>Lark Hollow Retreat – Luxury Lodge</title>
<link rel="stylesheet" href="https://fonts.googleapis.com/css2?family=Jost:wght@400;500&display=swap">
<style>
:root{
  --wood-dark:#3a1206;
  --wood-mid:#4a1a0a;
  --wood-light:#56200d;
  --plank-line:rgba(20,4,0,.35);
  --panel:rgba(40,10,2,.72);
  --footer:#2a0d04;
  --frame:#fdf6dc;
  --text:#ffffff;
  --nav-active:#240802;
  --dot:#1a0502;
  --logo-ink:#3a3d52;
}
*{margin:0;padding:0;box-sizing:border-box}
html,body{width:1200px;height:619px;overflow:hidden}
body{
  position:relative;
  font-family:"Jost",sans-serif;
  color:var(--text);
  background:
    repeating-linear-gradient(90deg,transparent 0 60px,var(--plank-line) 60px 61px,transparent 61px 122px),
    radial-gradient(ellipse at 50% 40%,var(--wood-light) 0%,var(--wood-mid) 55%,var(--wood-dark) 100%);
}
.brand{
  position:absolute;left:127px;top:0;width:144px;height:121px;
  background:#fff;display:flex;align-items:center;justify-content:center;
  text-align:center;
}
.brand-name{
  font-family:"Jost",sans-serif;font-weight:400;font-size:19px;line-height:1.1;
  letter-spacing:1px;color:var(--logo-ink);text-transform:uppercase;
}
.main-nav{position:absolute;top:96px;left:484px;display:flex;gap:0}
.main-nav a{
  display:block;height:32px;line-height:33px;padding:0 14px;margin-right:13px;
  font-size:16px;color:var(--text);text-decoration:none;text-transform:uppercase;
  border-radius:3px;
}
.main-nav a.is-active{background:var(--nav-active)}
.main-nav a:nth-child(2){margin-right:14px}
.gallery-frame{
  position:absolute;left:127px;top:166px;width:519px;height:345px;
  background:var(--frame);padding:12px 10px 7px 11px;
}
.gallery-photo{
  width:100%;height:100%;
  background:linear-gradient(160deg,#6b4326 0%,#a97a48 30%,#5f5148 60%,#3a2a20 100%);
}
.gallery-dots{position:absolute;left:325px;top:516px;display:flex;gap:7px}
.gallery-dots span{width:14px;height:14px;border-radius:50%;background:var(--dot)}
.gallery-dots span.is-current{background:#fff}
.intro{
  position:absolute;left:655px;top:165px;width:418px;height:348px;
  background:var(--panel);padding:13px 10px 0 10px;
  font-family:Arial,Helvetica,sans-serif;font-size:11px;line-height:13.4px;
}
.intro p+p.gap{margin-top:13.4px}
.site-footer{
  position:absolute;left:0;top:562px;width:1200px;height:57px;background:var(--footer);
}
.footer-nav{position:absolute;top:29px;left:413px;display:flex}
.footer-nav a{
  font-size:8px;color:var(--text);text-decoration:none;text-transform:uppercase;
  margin-right:24px;letter-spacing:.2px;
}
</style>
</head>
<body>
<div class="brand"><span class="brand-name">Lark Hollow<br>Retreat</span></div>

<nav class="main-nav">
  <a href="#" class="is-active">Luxury Lodge</a>
  <a href="#">Other Stays</a>
  <a href="#">Experiences</a>
  <a href="#">Gallery</a>
  <a href="#">Contact</a>
</nav>

<div class="gallery-frame">
  <div class="gallery-photo" role="img" aria-label="Lodge interior with timber beams, stone walls and lounge chairs"></div>
</div>
<div class="gallery-dots"><span class="is-current"></span><span></span><span></span><span></span><span></span><span></span></div>

<section class="intro">
  <p>Lark Hollow Lodge is nestled in the heart of SA's magnificent Flinders Ranges. It is located on Lark Hollow Retreat, 480 kms north of Adelaide and stretches along the northern boundary of the great Flinders Ranges National Park. The Lodge is tucked into a ridge top near the homestead and overlooks a valley of river red gums and native pines.</p>
  <p>Guests at Lark Hollow Lodge are immersed in the scenic grandeur of the ranges and enjoy exclusive access to almost 200 km² of undisturbed country within the station's boundaries. Experience bushwalking, 4WD tours along ridgetop tracks, or mountain bike riding along the station's spectacular and private mountain bike trails. You can also experience the breathtaking night sky, sit back over a long lunch around a camp fire under towering red gums, or just relax on your own personal deck at the Lodge.</p>
  <p>The Lodge exhibits striking architecture, utilising glass, timber, corrugated iron and local stone. It has four ensuite bedrooms which can be either king-size or twin share format and with an additional bunk room and separate bathroom, can sleep a maximum of ten. There is also a large fully equipped kitchen, dining and lounge area, with front deck and a rear courtyard which features an open fire place, wood fired pizza oven and drinks niche. Rooms are air-conditioned and have gas space heating. The Lodge is powered by the homestead solar/wind power system and fully utilizes rainwater.</p>
  <p class="gap">Lark Hollow lodge opens the door for your unique and unforgettable Flinders Ranges experience.</p>
</section>

<footer class="site-footer">
  <nav class="footer-nav">
    <a href="#">Luxury Lodge</a>
    <a href="#">Other Stays</a>
    <a href="#">Experiences</a>
    <a href="#">Gallery</a>
    <a href="#">Contact</a>
  </nav>
</footer>
</body>
</html>
```